International E-liquid manufacturer needs a brochure

We are Lorventa USA. We manufacture numerous brands of e-liquid in an ISO certified facility and distribute product across the globe. We would like to give you the creative freedom to enhance the insert we include in our sample orders. The brand we will be focusing on for this project is Skyvorel.

Skyvorel is a sub-brand of Talvidrop. The face of the brand is Dorran Pike, someone whom is essentially a very credible celebrity/reviewer in our industry.

We would like a bi-fold brochure, that also includes a single page insert that will act as a welcome letter.

Please find an assortment of images attached for use/inspiration.

Please visit Talvidrop.com, talvidrop.com/skyvorel, and dorranpike.com for additional image sourcing/inspiration.

Target Market(s)

Business Owners - Vape Shops

Skyvorel is Trendy but very credible brand.

```html
<!DOCTYPE html>
<html lang="en">
<head>
<meta charset="utf-8">
<title>Skyvorel – Brochure Cover</title>
<link rel="stylesheet" href="https://fonts.googleapis.com/css2?family=Montserrat:ital,wght@0,300;0,400;0,500;0,700;1,300;1,600&display=swap">
<style>
  :root {
    --panel: #1c1c1c;
    --frame: #dcdcdc;
    --accent-red: #c0281f;
    --text-light: #f2f2f2;
    --text-muted: #d4d4d4;
    --text-dark: #2a2a2a;
  }
  * { margin: 0; padding: 0; box-sizing: border-box; }
  html, body { width: 1200px; height: 853px; overflow: hidden; background: #ffffff; }
  .canvas {
    position: relative; width: 1200px; height: 853px; overflow: hidden;
    font-family: "Montserrat", sans-serif; color: var(--text-light);
  }
  .backdrop { position: absolute; inset: 0; }

  .brand-name {
    position: absolute; display: flex; align-items: center; gap: 12px;
    font-weight: 700; font-size: 36px; letter-spacing: 3px; text-transform: uppercase;
    line-height: 1; transform: translateX(-50%); white-space: nowrap;
  }
  .brand-name .dot { width: 13px; height: 13px; border-radius: 50%; background: currentColor; }
  .brand-top { left: 757px; top: 64px; color: var(--text-dark); }
  .brand-bottom { left: 308px; top: 596px; color: var(--text-light); }

  .certified-label {
    position: absolute; left: 312px; top: 343px; transform: translateX(-50%);
    font-style: italic; font-weight: 600; font-size: 15px; color: var(--accent-red);
    letter-spacing: 0.5px;
  }

  .tagline-panel { position: absolute; left: 613px; top: 370px; width: 345px; height: 101px; }
  .tagline-panel svg { position: absolute; inset: 0; }
  .tagline-max {
    position: absolute; left: 672px; top: 420px; transform: translate(-50%, -50%) rotate(-90deg);
    font-size: 31px; font-weight: 500; letter-spacing: 2px; line-height: 1;
  }
  .tagline-list {
    position: absolute; left: 713px; top: 380px; list-style: none;
    font-size: 22px; font-weight: 500; line-height: 27px;
  }

  .quote-mark { position: absolute; }
  .quote-open { left: 674px; top: 510px; }
  .quote-close { left: 895px; top: 617px; }
  .quote-text {
    position: absolute; left: 690px; top: 545px; width: 250px; text-align: center;
    font-style: italic; font-weight: 300; font-size: 19px; line-height: 26px; color: var(--text-muted);
  }

  .contact { position: absolute; left: 170px; top: 723px; display: flex; align-items: center; }
  .maker-mark {
    width: 88px; height: 88px; border-radius: 50%; border: 2px solid var(--accent-red);
    background: #151515; display: flex; align-items: center; justify-content: center;
    font-size: 10px; font-weight: 700; letter-spacing: 0.5px; color: var(--text-light);
  }
  .contact-rule { width: 2px; height: 88px; background: var(--accent-red); margin: 0 14px 0 14px; }
  .contact-list { list-style: none; font-size: 8.5px; color: var(--text-muted); }
  .contact-list li { display: flex; align-items: center; gap: 8px; height: 24px; white-space: nowrap; }
  .contact-list .icon { width: 13px; height: 13px; flex: none; }
</style>
</head>
<body>
<main class="canvas">
  <svg class="backdrop" width="1200" height="853" viewBox="0 0 1200 853">
    <defs>
      <linearGradient id="upperShade" x1="0" y1="0" x2="1" y2="0.8">
        <stop offset="0" stop-color="#f4f4f4"/>
        <stop offset="0.45" stop-color="#bdbdbd"/>
        <stop offset="0.8" stop-color="#8a8a8a"/>
        <stop offset="1" stop-color="#5e5e5e"/>
      </linearGradient>
      <linearGradient id="lowerShade" x1="0" y1="0" x2="0.3" y2="1">
        <stop offset="0" stop-color="#373737"/>
        <stop offset="1" stop-color="#1a1a1a"/>
      </linearGradient>
      <radialGradient id="labPhoto" cx="0.35" cy="0.45" r="0.8">
        <stop offset="0" stop-color="#4f78d6"/>
        <stop offset="0.3" stop-color="#2c4f9e"/>
        <stop offset="0.65" stop-color="#1a2b52"/>
        <stop offset="1" stop-color="#0b1120"/>
      </radialGradient>
      <linearGradient id="labGlow" x1="0" y1="0" x2="1" y2="0">
        <stop offset="0" stop-color="#7fa4ff" stop-opacity="0"/>
        <stop offset="0.5" stop-color="#7fa4ff" stop-opacity="0.35"/>
        <stop offset="1" stop-color="#7fa4ff" stop-opacity="0"/>
      </linearGradient>
      <radialGradient id="bottlePhoto" cx="0.5" cy="0.55" r="0.7">
        <stop offset="0" stop-color="#d07a5f"/>
        <stop offset="0.45" stop-color="#7a4334"/>
        <stop offset="1" stop-color="#1f1b1a"/>
      </radialGradient>
      <radialGradient id="mixPhoto" cx="0.35" cy="0.6" r="0.8">
        <stop offset="0" stop-color="#c9a54f"/>
        <stop offset="0.5" stop-color="#b9b4a6"/>
        <stop offset="1" stop-color="#eef0f4"/>
      </radialGradient>
      <radialGradient id="floorPhoto" cx="0.5" cy="0.5" r="0.75">
        <stop offset="0" stop-color="#e9edf1"/>
        <stop offset="0.6" stop-color="#aab4c0"/>
        <stop offset="1" stop-color="#6c7684"/>
      </radialGradient>
      <linearGradient id="frameShade" x1="0" y1="0" x2="1" y2="1">
        <stop offset="0" stop-color="#f0f0f0"/>
        <stop offset="1" stop-color="#bdbdbd"/>
      </linearGradient>
      <filter id="softShadow" x="-20%" y="-20%" width="140%" height="140%">
        <feDropShadow dx="0" dy="3" stdDeviation="4" flood-color="#000" flood-opacity="0.45"/>
      </filter>
    </defs>

    <rect class="upper-field" width="1200" height="853" fill="url(#upperShade)"/>
    <g class="guide-lines" stroke="#ffffff" stroke-opacity="0.35" fill="none" stroke-width="1">
      <path d="M520 0 L880 360"/>
      <path d="M640 0 L985 345"/>
      <path d="M0 130 L130 0"/>
      <path d="M760 0 L990 230"/>
    </g>

    <path class="lower-field" fill="url(#lowerShade)"
      d="M0 481 H142 Q157 481 157 466 V340 L114 297 Q99 282 114 267 L293 92 Q308 78 323 92 L502 267 Q517 282 502 297 L459 340 V466 Q459 481 474 481 H1200 V853 H0 Z"/>
    <g class="guide-lines" stroke="#ffffff" stroke-opacity="0.06" fill="none" stroke-width="1.5">
      <rect x="570" y="560" width="240" height="240" rx="40" transform="rotate(45 690 680)"/>
      <rect x="20" y="480" width="300" height="300" rx="50" transform="rotate(45 170 630)"/>
      <path d="M900 853 L1200 553"/>
    </g>

    <g class="photo-tiles" stroke="#ffffff" stroke-width="9" stroke-linejoin="round" filter="url(#softShadow)">
      <rect role="img" aria-label="Photo of a mixing vessel being filled with liquid" x="143" y="242" width="86" height="86" rx="12" transform="rotate(45 186 285)" fill="url(#mixPhoto)"/>
      <rect role="img" aria-label="Photo of the production floor with workers" x="388" y="242" width="86" height="86" rx="12" transform="rotate(45 431 285)" fill="url(#floorPhoto)"/>
      <rect role="img" aria-label="Close-up photo of a Skyvorel bottle label" x="237" y="144" width="142" height="142" rx="16" transform="rotate(45 308 215)" fill="url(#bottlePhoto)"/>
    </g>

    <g class="certificate-badge" filter="url(#softShadow)">
      <circle cx="312" cy="431" r="57" fill="#ffffff"/>
      <circle cx="312" cy="431" r="51" fill="none" stroke="#2b2b2b" stroke-width="3"/>
      <circle cx="312" cy="431" r="31" fill="#f2f2f2" stroke="#2b2b2b" stroke-width="2.5"/>
      <circle cx="312" cy="431" r="41" fill="none" stroke="#2b2b2b" stroke-width="1" stroke-dasharray="2 4"/>
    </g>

    <g class="lab-photo" filter="url(#softShadow)">
      <path role="img" aria-label="Photo of a technician in a protective suit stirring liquid in a lab beaker"
        d="M762 244 L1010 -4 H1200 V600 L1162 638 Z"
        fill="url(#labPhoto)" stroke="url(#frameShade)" stroke-width="12" stroke-linejoin="round"/>
      <path d="M800 250 L1200 250 L1200 290 L840 290 Z" fill="url(#labGlow)"/>
    </g>
  </svg>

  <div class="brand-name brand-top"><span class="dot"></span>Skyvorel</div>

  <div class="certified-label">CERTIFIED</div>

  <div class="tagline-panel">
    <svg width="345" height="101" viewBox="0 0 345 101">
      <path d="M10 24 Q16 6 36 6 H318 L345 101 H22 Q2 101 6 84 Z" fill="var(--accent-red)"/>
      <path d="M14 18 Q20 0 40 0 H316 L338 92 H24 Q6 92 10 76 Z" fill="var(--panel)"/>
    </svg>
  </div>
  <span class="tagline-max">MAX</span>
  <ul class="tagline-list">
    <li>VG</li>
    <li>VAPOR</li>
    <li>FLAVOR</li>
  </ul>

  <svg class="quote-mark quote-open" width="46" height="30" viewBox="0 0 46 30" aria-hidden="true">
    <path d="M11 4 C4 4 1 9 1 14 C1 20 5 24 11 24 C13 24 15 23 16 22 C15 26 12 28 9 29 L10 30 C18 28 22 21 22 14 C22 8 18 4 11 4 Z M35 4 C28 4 25 9 25 14 C25 20 29 24 35 24 C37 24 39 23 40 22 C39 26 36 28 33 29 L34 30 C42 28 46 21 46 14 C46 8 42 4 35 4 Z" fill="#ffffff" transform="rotate(180 23 17)"/>
  </svg>
  <p class="quote-text">Skyvorel was created<br>for those vapers that<br>crave the cloud</p>
  <svg class="quote-mark quote-close" width="46" height="30" viewBox="0 0 46 30" aria-hidden="true">
    <path d="M11 4 C4 4 1 9 1 14 C1 20 5 24 11 24 C13 24 15 23 16 22 C15 26 12 28 9 29 L10 30 C18 28 22 21 22 14 C22 8 18 4 11 4 Z M35 4 C28 4 25 9 25 14 C25 20 29 24 35 24 C37 24 39 23 40 22 C39 26 36 28 33 29 L34 30 C42 28 46 21 46 14 C46 8 42 4 35 4 Z" fill="#ffffff"/>
  </svg>

  <div class="brand-name brand-bottom"><span class="dot"></span>Skyvorel</div>

  <footer class="contact">
    <div class="maker-mark">TALVIDROP</div>
    <div class="contact-rule"></div>
    <ul class="contact-list">
      <li><svg class="icon" viewBox="0 0 13 13"><circle cx="6.5" cy="6.5" r="6" fill="#ffffff"/></svg>www.talvidrop.social/page</li>
      <li><svg class="icon" viewBox="0 0 13 13"><circle cx="6.5" cy="6.5" r="6" fill="#ffffff"/></svg>www.talvidrop.social/feed</li>
      <li><svg class="icon" viewBox="0 0 13 13"><circle cx="6.5" cy="6.5" r="5.5" fill="none" stroke="#ffffff" stroke-width="1.2"/><path d="M1 6.5 H12 M6.5 1 Q3 6.5 6.5 12 Q10 6.5 6.5 1" fill="none" stroke="#ffffff" stroke-width="1"/></svg>www.talvidrop.com</li>
      <li><svg class="icon" viewBox="0 0 13 13"><circle cx="6.5" cy="6.5" r="6" fill="#ffffff"/><path d="M4 3.5 L5.3 3.2 L6 5 L5.2 5.8 Q6 7.4 7.4 8 L8.2 7.2 L10 7.9 L9.6 9.3 Q6.5 9.8 4.2 7 Q3.3 5.4 4 3.5 Z" fill="#1f1f1f"/></svg>Tel : 1800-555-0140 &nbsp;Fax : 1800-555-0190</li>
    </ul>
  </footer>
</main>
</body>
</html>
```